Business card design needed

I would like a one sided black business card with the information provided above. Refer to my website www.lobcrafttennis.com.au for an example of colors I have used for my site, would like to keep this consistent for my business cards also, I will upload my logo below.

I am a new small business that provides tennis customers with racquet re stringing, tennis strings and accessories.

Industry/Entity Type

Small Business

Contact Information for Business Card

Lob Craft Tennis

Dennis Morrow
Managing Director

lobcrafttennis@mailbay.com
www.lobcrafttennis.com.au
0412 695 203

Racquet Restringing/Tennis Strings/Accessories

Requirements
Must have
• Must have my logo and card must be black

```html
<!DOCTYPE html>
<html lang="en">
<head>
<meta charset="utf-8">
<title>Lob Craft Tennis – Business Card</title>
<link rel="stylesheet" href="https://fonts.googleapis.com/css2?family=Pathway+Gothic+One&display=swap">
<style>
  :root {
    --card-black: #000000;
    --divider-white: #ffffff;
    --lime: #c8e03c;
    --label-grey: #8a8a8a;
    --sphere-light: #2a2a2a;
    --sphere-dark: #050505;
    --mark-grey: #5a5a5a;
  }
  * { margin: 0; padding: 0; box-sizing: border-box; }
  html, body {
    width: 978px;
    height: 1200px;
    overflow: hidden;
    background: var(--divider-white);
    font-family: "Pathway Gothic One", "Arial Narrow", sans-serif;
  }
  .sheet { position: relative; width: 978px; height: 1200px; }
  .card {
    position: absolute;
    left: 0;
    width: 978px;
    background: var(--card-black);
    overflow: hidden;
  }
  .card--front { top: 0; height: 601px; }
  .card--back { top: 615px; height: 585px; }

  .halftone-sphere {
    position: absolute;
    left: 231px;
    top: 15px;
    width: 530px;
    height: 530px;
    border-radius: 50%;
    background: radial-gradient(circle at 50% 38%, var(--sphere-light) 0%, #1a1a1a 45%, var(--sphere-dark) 75%, var(--card-black) 100%);
  }

  .brand {
    position: absolute;
    left: 0;
    width: 100%;
    display: flex;
    justify-content: center;
    align-items: center;
    gap: 14px;
    letter-spacing: 2px;
    text-transform: uppercase;
    white-space: nowrap;
  }
  .brand__dot {
    border-radius: 50%;
    flex: none;
  }
  .card--front .brand { top: 160px; font-size: 52px; color: var(--lime); }
  .card--front .brand__dot { width: 30px; height: 30px; background: var(--lime); }
  .card--back .brand { top: 272px; font-size: 64px; color: var(--mark-grey); }
  .card--back .brand__dot { width: 36px; height: 36px; background: var(--mark-grey); }

  .details {
    position: absolute;
    top: 312px;
    left: 0;
    width: 100%;
    display: grid;
    grid-template-columns: 426px 1fr;
    column-gap: 17px;
    row-gap: 14px;
    font-size: 16px;
    line-height: 24px;
    letter-spacing: 0.3px;
  }
  .details__label { text-align: right; color: var(--label-grey); }
  .details__value { color: var(--lime); }
</style>
</head>
<body>
<main class="sheet">
  <section class="card card--front">
    <div class="halftone-sphere" role="img" aria-label="Halftone dot sphere pattern in dark grey"></div>
    <div class="brand">
      <span class="brand__dot"></span>
      <span class="brand__name">Lob Craft Tennis</span>
    </div>
    <dl class="details">
      <dt class="details__label">Company&nbsp; Name</dt>
      <dd class="details__value">Lob Craft Tennis Dennis Morrow</dd>
      <dt class="details__label">Managing Director -Mail</dt>
      <dd class="details__value">Managing Director lobcrafttennis@mailbay.com</dd>
      <dt class="details__label">Website Address</dt>
      <dd class="details__value">www.lobcrafttennis.com.au 0412 695 203</dd>
      <dt class="details__label"></dt>
      <dd class="details__value">Racquet Restringing/Tennis Strings/Accessories</dd>
    </dl>
  </section>

  <section class="card card--back">
    <div class="brand">
      <span class="brand__dot"></span>
      <span class="brand__name">Lob Craft Tennis</span>
    </div>
  </section>
</main>
</body>
</html>
```